Gift box company needs packaging design for shipping box

We need a design to decorate our brown cardboard shipping boxes. The design must include our company logo (provided) and a "fragile" label somewhere. We will be using single colour printing so the design must only be in one colour. As it will be covering a brown box, I think black or dark blue would be most appropriate. The shipping box itself measures 355mm wide X 246mm deep X 105mm tall. If the design could make the box look like a wrapped present in some way, that would be great.

```html
<!DOCTYPE html>
<html lang="en">
<head>
<meta charset="utf-8">
<title>Kindly Sent – Shipping Box Artwork</title>
<link href="https://fonts.googleapis.com/css2?family=Jost:wght@400;600;700&display=swap" rel="stylesheet">
<style>
  :root {
    --ink: #1e1e1e;
    --paper: #ffffff;
  }
  html, body {
    margin: 0;
    padding: 0;
    width: 1200px;
    height: 1200px;
    overflow: hidden;
    background: var(--paper);
  }
  .artwork {
    display: block;
    width: 1200px;
    height: 1200px;
  }
  .ink { fill: var(--ink); }
  .paper { fill: var(--paper); }
  .label-text {
    font-family: "Jost", sans-serif;
    font-size: 5.6px;
    font-weight: 600;
    letter-spacing: 0.4px;
    fill: var(--ink);
  }
  .label-rule {
    stroke: var(--ink);
    stroke-width: 0.8;
    stroke-dasharray: 0.8 1.6;
  }
  .fragile-text {
    font-family: "Jost", sans-serif;
    font-size: 15px;
    font-weight: 700;
    letter-spacing: 2px;
    fill: var(--ink);
  }
  .fragile-tick { stroke: var(--ink); stroke-width: 2; stroke-dasharray: 3 6; }
  .brand-name {
    font-family: "Jost", sans-serif;
    font-size: 15px;
    font-weight: 600;
    fill: var(--ink);
  }
</style>
</head>
<body>
<svg class="artwork" viewBox="0 0 1200 1200" xmlns="http://www.w3.org/2000/svg">
  <defs>
    <pattern id="lid-stripes" width="13.2" height="10" patternUnits="userSpaceOnUse">
      <rect class="ink" x="0" y="0" width="3.6" height="10"/>
    </pattern>
    <pattern id="side-stripes" width="12.7" height="10" patternUnits="userSpaceOnUse">
      <rect class="ink" x="0" y="0" width="3.4" height="10"/>
    </pattern>
  </defs>

  <!-- Lid panel -->
  <g class="lid-panel" transform="translate(51 484)">
    <rect x="0" y="0" width="480" height="231" fill="url(#lid-stripes)"/>
    <rect class="ink ribbon-vertical" x="219" y="0" width="41" height="231"/>
    <rect class="ink ribbon-horizontal" x="0" y="146" width="480" height="42"/>
    <g class="bow" role="img" aria-label="Flower-shaped ribbon bow illustration">
      <circle class="paper" cx="237" cy="165" r="68"/>
      <circle class="ink" cx="237" cy="165" r="60"/>
    </g>
  </g>

  <!-- Side panel -->
  <g class="side-panel" transform="translate(591 570)">
    <rect x="0" y="0" width="518" height="153" fill="url(#side-stripes)"/>
    <rect class="ink ribbon-band" x="237" y="0" width="45" height="153"/>

    <g class="brand-mark">
      <rect class="paper" x="22" y="64" width="94" height="40"/>
      <text class="brand-name" x="69" y="89" text-anchor="middle">Kindly Sent</text>
    </g>

    <g class="gift-label">
      <rect class="paper" x="414" y="0" width="98" height="153"/>
      <text class="label-text" x="418" y="24">TO:</text>
      <line class="label-rule" x1="431" y1="24" x2="508" y2="24"/>
      <text class="label-text" x="418" y="41">MESSAGE:</text>
      <line class="label-rule" x1="451" y1="41" x2="508" y2="41"/>
      <line class="label-rule" x1="418" y1="58" x2="508" y2="58"/>
      <line class="label-rule" x1="418" y1="74" x2="508" y2="74"/>
      <line class="label-rule" x1="418" y1="90" x2="508" y2="90"/>
      <text class="label-text" x="418" y="112">FROM:</text>
      <line class="label-rule" x1="440" y1="112" x2="508" y2="112"/>
      <line class="fragile-tick" x1="418" y1="121" x2="508" y2="121"/>
      <text class="fragile-text" x="418" y="141">FRAGILE</text>
      <line class="fragile-tick" x1="418" y1="151" x2="508" y2="151"/>
    </g>
  </g>
</svg>
</body>
</html>
```